Brightway Rehab Florida Billboard

We need a billboard designed for our physical therapy practice. Our billboard also serves as the sign for our building. We would like to have some sort of graphic notifying people driving by that our building is located here. Please go to www.brightwayrehabfl-example.com in order to get a better idea of our company.

Target Market(s)

Senior citizens having physical therapy

Industry/Entity Type

Healthcare- Physical Therapy

Colors
0094D4
00A9DD
6FCCEA
C7EBF8
E9F6FB

Requirements
Must have
• Must contain in bold the words "physical therapy". Must be highly visible from the road and have our company colors incorporated. Would also like to use the phrase "Relieving Pain. Restoring Function. Improving Lives."

```html
<!DOCTYPE html>
<html lang="en">
<head>
<meta charset="utf-8">
<title>Brightway Rehab Florida Billboard</title>
<link href="https://fonts.googleapis.com/css2?family=Barlow+Condensed:wght@600;800&family=Montserrat:wght@500&display=swap" rel="stylesheet">
<style>
  :root{
    --sky:#C7EBF8;
    --light:#6FCCEA;
    --mid:#00A9DD;
    --brand:#0094D4;
    --deep:#0a5a8e;
    --band:#0b4f7c;
    --green:#86b52f;
    --green-dark:#4f7d18;
    --lime:#d6e83a;
    --white:#ffffff;
    --page:#ffffff;
  }
  *{margin:0;padding:0;box-sizing:border-box}
  html,body{width:1065px;height:1200px;overflow:hidden;background:var(--page)}
  .billboard{
    position:absolute;left:20px;top:429px;width:1025px;height:342px;overflow:hidden;
    background:linear-gradient(180deg,var(--sky) 0%,var(--light) 22%,var(--mid) 45%,var(--brand) 62%,var(--deep) 100%);
    font-family:'Barlow Condensed',sans-serif;
  }
  .billboard__sheen{position:absolute;inset:0}
  .headline{
    position:absolute;left:34px;top:18px;font-weight:800;font-size:94px;line-height:1;
    color:var(--white);letter-spacing:-1px;white-space:nowrap;
    -webkit-text-stroke:9px var(--green);paint-order:stroke fill;
    text-shadow:0 3px 0 var(--green-dark),0 6px 8px rgba(0,40,70,.35);
  }
  .promise-band{
    position:absolute;left:0;top:140px;width:810px;height:44px;background:var(--band);
    display:flex;align-items:center;gap:22px;padding-left:32px;
  }
  .promise{display:flex;align-items:center;gap:6px;color:var(--white);font-weight:600;font-size:29px;letter-spacing:.3px;white-space:nowrap}
  .tick{width:15px;height:15px}
  .contact{position:absolute;left:20px;display:flex;align-items:center;gap:14px;white-space:nowrap}
  .contact--phone{top:208px}
  .contact--web{top:278px}
  .contact__icon{width:44px;height:44px;flex:none}
  .phone-number{font-weight:800;font-size:60px;color:var(--lime);line-height:1;text-shadow:0 3px 5px rgba(0,30,60,.4)}
  .web-address{font-weight:600;font-size:28px;color:var(--white);line-height:1;text-shadow:0 3px 5px rgba(0,30,60,.4)}
  .brand-mark{position:absolute;left:484px;top:210px;width:110px;height:110px;border-radius:50%;background:var(--mid)}
  .brand-divider{position:absolute;left:606px;top:200px;width:3px;height:132px;background:var(--white)}
  .brand-name{
    position:absolute;left:620px;top:218px;font-family:'Montserrat',sans-serif;font-weight:500;
    font-size:21px;line-height:34px;letter-spacing:1.5px;color:var(--white);white-space:nowrap;
  }
  .therapy-photo{
    position:absolute;right:0;top:0;width:215px;height:342px;
    background:linear-gradient(160deg,#a9d6ee 0%,#7fbde0 35%,#e6eef3 65%,#9fb0bb 100%);
  }
</style>
</head>
<body>
  <section class="billboard">
    <svg class="billboard__sheen" width="1025" height="342" viewBox="0 0 1025 342" aria-hidden="true">
      <path d="M0 120 C250 60 500 150 810 90 L810 0 L0 0Z" fill="#ffffff" opacity=".12"/>
      <path d="M0 330 C300 250 520 320 810 240 L810 342 L0 342Z" fill="#04406a" opacity=".25"/>
    </svg>

    <h1 class="headline">PHYSICAL THERAPY</h1>

    <div class="promise-band">
      <span class="promise"><svg class="tick" viewBox="0 0 16 16"><circle cx="8" cy="8" r="8" fill="#86b52f"/><path d="M4.5 8.3l2.3 2.2 4.6-4.8" stroke="#fff" stroke-width="2" fill="none"/></svg>RELIEVING PAIN</span>
      <span class="promise"><svg class="tick" viewBox="0 0 16 16"><circle cx="8" cy="8" r="8" fill="#86b52f"/><path d="M4.5 8.3l2.3 2.2 4.6-4.8" stroke="#fff" stroke-width="2" fill="none"/></svg>RESTORING FUNCTION</span>
      <span class="promise"><svg class="tick" viewBox="0 0 16 16"><circle cx="8" cy="8" r="8" fill="#86b52f"/><path d="M4.5 8.3l2.3 2.2 4.6-4.8" stroke="#fff" stroke-width="2" fill="none"/></svg>IMPROVING LIVES</span>
    </div>

    <div class="contact contact--phone">
      <svg class="contact__icon" viewBox="0 0 48 48" aria-hidden="true">
        <circle cx="24" cy="24" r="23" fill="#86b52f"/>
        <path d="M17 13c1.5-1 3-.5 3.7.8l2 3.6c.6 1.1.3 2.3-.6 3l-1.6 1.2c1 2.6 3.3 5 6 6.2l1.3-1.6c.8-.9 2-1.1 3-.5l3.6 2.1c1.3.7 1.7 2.3.7 3.6l-1.7 2c-1.4 1.6-4 1.9-7 .5-5.8-2.6-10.7-7.9-12.6-13.7-.9-2.8-.5-5.3 1.2-6.7z" fill="#fff"/>
      </svg>
      <span class="phone-number">555-014-2290</span>
    </div>

    <div class="contact contact--web">
      <svg class="contact__icon" viewBox="0 0 48 48" aria-hidden="true">
        <circle cx="24" cy="24" r="23" fill="#86b52f"/>
        <circle cx="24" cy="24" r="12" fill="none" stroke="#fff" stroke-width="2.5"/>
        <ellipse cx="24" cy="24" rx="5" ry="12" fill="none" stroke="#fff" stroke-width="2"/>
        <path d="M12 24h24" stroke="#fff" stroke-width="2"/>
      </svg>
      <span class="web-address">www.brightwayrehabfl-example.com</span>
    </div>

    <div class="brand-mark" aria-hidden="true"></div>
    <div class="brand-divider" aria-hidden="true"></div>
    <p class="brand-name">BRIGHTWAY<br>REHAB<br>FLORIDA</p>

    <div class="therapy-photo" role="img" aria-label="Photo of a physical therapist in blue scrubs guiding a smiling senior woman through an arm-stretching exercise"></div>
  </section>
</body>
</html>
```